Bright Harbor Construction

We are a commercial construction company specializing in steel stud framing, drywall, taping and acoustical ceilings. We would like a company logo (Something that looks great and isnt boring) as we have not been able to come up with one. A modern looking card would definitely suit our personalities best
Updates

We would like to try and avoid using dark colors. I have learned from experience that dark colors are the last to looked at. Thank you

```html
<!DOCTYPE html>
<html lang="en">
<head>
<meta charset="utf-8">
<title>Bright Harbor Construction – Business Card</title>
<link rel="stylesheet" href="https://fonts.googleapis.com/css2?family=Exo+2:wght@500&family=Open+Sans:wght@400;600&display=swap">
<style>
  :root {
    --page-bg: #e4e6e9;
    --card-bg: #f4f4f3;
    --brand-blue: #4fb1e2;
    --text-grey: #7a7b7d;
    --brand-grey: #8a8b8d;
  }
  * { margin: 0; padding: 0; box-sizing: border-box; }
  html, body {
    width: 1200px;
    height: 936px;
    overflow: hidden;
    background: var(--page-bg);
  }
  .card {
    position: absolute;
    left: 100px;
    top: 163px;
    width: 1000px;
    height: 610px;
    background: var(--card-bg);
    box-shadow: 0 6px 24px rgba(0, 0, 0, 0.12);
    font-family: "Open Sans", sans-serif;
    color: var(--text-grey);
  }
  .brand {
    position: absolute;
    left: 115px;
    top: 54px;
    display: flex;
    align-items: center;
    gap: 22px;
  }
  .brand-square {
    width: 108px;
    height: 108px;
    border: 3px solid var(--brand-blue);
  }
  .brand-name {
    font-family: "Open Sans", sans-serif;
    font-weight: 600;
    font-size: 29px;
    line-height: 1.2;
    letter-spacing: 1px;
    text-transform: uppercase;
    color: var(--brand-grey);
  }
  .person-name {
    position: absolute;
    left: 646px;
    top: 120px;
    font-family: "Exo 2", sans-serif;
    font-weight: 500;
    font-size: 36px;
    letter-spacing: 0.5px;
    color: var(--brand-blue);
    text-transform: uppercase;
  }
  .contact-list {
    position: absolute;
    left: 644px;
    top: 245px;
    list-style: none;
  }
  .contact-item {
    display: flex;
    align-items: center;
    gap: 12px;
    height: 37px;
    font-size: 26px;
  }
  .contact-icon {
    width: 25px;
    height: 25px;
    flex: none;
  }
  .web-highlight {
    color: var(--brand-blue);
    font-weight: 600;
  }
  .divider {
    position: absolute;
    left: 644px;
    top: 402px;
    width: 25px;
    height: 2px;
    background: var(--brand-blue);
  }
  .address {
    position: absolute;
    left: 644px;
    top: 456px;
    font-size: 26px;
    line-height: 32px;
    font-style: normal;
  }
</style>
</head>
<body>
  <div class="card">
    <div class="brand">
      <div class="brand-square"></div>
      <div class="brand-name">Bright Harbor<br>Construction</div>
    </div>

    <div class="person-name">Dana Whitfield</div>

    <ul class="contact-list">
      <li class="contact-item">
        <svg class="contact-icon" viewBox="0 0 24 24" fill="none" stroke="#4fb1e2" stroke-width="1.6" stroke-linecap="round" stroke-linejoin="round">
          <path d="M12 2.5a9.5 9.5 0 0 0-8.2 14.3L2.5 21.5l4.8-1.3A9.5 9.5 0 1 0 12 2.5z"/>
          <path d="M8.6 7.6c.4-.4 1-.4 1.3 0l1 1.4c.3.4.2.9-.1 1.2l-.5.5c.6 1.3 1.6 2.3 2.9 2.9l.5-.5c.3-.3.8-.4 1.2-.1l1.4 1c.4.3.4.9 0 1.3l-.7.7c-.6.6-1.6.7-2.4.3a10 10 0 0 1-4.6-4.6c-.4-.8-.3-1.8.3-2.4z"/>
        </svg>
        <span>(555)010-0199</span>
      </li>
      <li class="contact-item">
        <svg class="contact-icon" viewBox="0 0 24 24" fill="none" stroke="#4fb1e2" stroke-width="1.6" stroke-linejoin="round">
          <rect x="2" y="5" width="20" height="14"/>
          <path d="M2 5l10 8 10-8M2 19l7.5-7.5M22 19l-7.5-7.5"/>
        </svg>
        <span>sales@bhcbuild.com</span>
      </li>
      <li class="contact-item">
        <svg class="contact-icon" viewBox="0 0 24 24" fill="none" stroke="#4fb1e2" stroke-width="1.6">
          <circle cx="12" cy="12" r="10" fill="#4fb1e2" stroke="none"/>
          <path d="M2 12h20M12 2v20M4 7h16M4 17h16" stroke="#f4f4f3" stroke-width="1.3"/>
          <ellipse cx="12" cy="12" rx="4.5" ry="10" stroke="#f4f4f3" stroke-width="1.3"/>
        </svg>
        <span>www.<span class="web-highlight">bhcbuild</span>.com</span>
      </li>
    </ul>

    <div class="divider"></div>

    <address class="address">
      Alderwood Ct.<br>
      Suite 210<br>
      Maplestone, Georgia 30999
    </address>
  </div>
</body>
</html>
```